Corvane Holdings , new business card design

investment firm with corporate clients . need double sided business card , vertical and horizontal options ,logo must be clear. prefer pantone colors only and sharp design. website also www.corvane-example.ae

Khalid Bin Rashed
Managing Director
Tel. +971 4 000 3829
Mobile +971 50 000 4172
khalid@corvane-example.ae
Palm Crest Tower, officw 18-B07, Qasr Gardens, Dubai

Contact Information for Business Card

Khalid Bin Rashed
Managing Director

Font styles to use
Serif

Colors

Designer to choose colors to be used in the design.

```html
<!DOCTYPE html>
<html lang="en">
<head>
<meta charset="utf-8">
<title>Corvane Holdings – Business Card</title>
<link rel="stylesheet" href="https://fonts.googleapis.com/css2?family=Roboto:wght@300;400;700&display=swap">
<style>
  :root {
    --page-bg: #2a2d33;
    --card-light: #c9c9cd;
    --card-navy: #0b2a6e;
    --ink: #17191f;
    --ink-soft: #3c3f46;
    --accent-blue: #3d7fd9;
    --rule-blue: #123a9a;
    --rule-light: #6f86b8;
    --steel: #8fa6c4;
    --web-ink: #06163d;
  }
  * { margin: 0; padding: 0; box-sizing: border-box; }
  html, body {
    width: 1200px; height: 900px; overflow: hidden;
    background: var(--page-bg);
    font-family: "Roboto", Arial, sans-serif;
  }
  .canvas {
    position: relative; width: 1200px; height: 900px;
    display: flex; flex-direction: column; align-items: center; justify-content: center; gap: 56px;
  }
  .card {
    position: relative; width: 560px; height: 320px;
    box-shadow: 0 10px 28px rgba(0,0,0,.45);
  }
  .card--front { background: var(--card-light); }
  .card--back { background: var(--card-navy); }

  .wordmark {
    position: absolute; display: flex; align-items: center; gap: 12px;
    font-weight: 300; letter-spacing: 4px; text-transform: uppercase;
    color: var(--ink); white-space: nowrap;
  }
  .wordmark__square { width: 14px; height: 14px; background: var(--steel); flex: none; }
  .card--front .wordmark { left: 38px; top: 46px; font-size: 30px; }
  .card--back .wordmark { left: 50%; top: 118px; transform: translateX(-50%); font-size: 34px; color: #030c24; }

  .contact-rule {
    position: absolute; left: 214px; top: 176px; width: 2px; height: 118px;
    background: var(--rule-blue);
  }
  .contact {
    position: absolute; left: 232px; top: 172px; color: var(--ink);
  }
  .contact__name { font-size: 21px; font-weight: 700; color: var(--accent-blue); line-height: 1.1; }
  .contact__title { font-size: 13px; font-weight: 400; color: var(--ink-soft); margin-bottom: 8px; }
  .contact__row { display: flex; align-items: flex-start; gap: 8px; margin-top: 4px; }
  .contact__icon { width: 20px; height: 20px; flex: none; }
  .contact__text { font-size: 12px; font-weight: 700; line-height: 1.3; }

  .website {
    position: absolute; left: 0; right: 0; bottom: 34px;
    display: flex; align-items: center; gap: 14px; padding: 0 0;
  }
  .website__line { flex: 1; height: 1px; background: var(--rule-light); }
  .website__text { font-size: 15px; font-weight: 700; color: var(--web-ink); }
</style>
</head>
<body>
<main class="canvas">

  <section class="card card--front" aria-label="Business card front">
    <div class="wordmark"><span class="wordmark__square"></span>Corvane Holdings</div>
    <div class="contact-rule"></div>
    <div class="contact">
      <p class="contact__name">Khalid Bin Rashed</p>
      <p class="contact__title">Managing Director</p>

      <div class="contact__row">
        <svg class="contact__icon" viewBox="0 0 20 20" aria-hidden="true">
          <circle cx="10" cy="10" r="10" fill="#1a1c22"/>
          <path d="M5 10 L10 5.5 L15 10 M6.5 9 V14.5 H13.5 V9" fill="none" stroke="#6f9be0" stroke-width="1.3"/>
        </svg>
        <p class="contact__text">Palm Crest Tower, officw 18-B07,<br>Qasr Gardens, Dubai</p>
      </div>

      <div class="contact__row">
        <svg class="contact__icon" viewBox="0 0 20 20" aria-hidden="true">
          <circle cx="10" cy="10" r="10" fill="#1a1c22"/>
          <rect x="6.5" y="5" width="7" height="10" rx="1.2" fill="none" stroke="#6f9be0" stroke-width="1.3"/>
          <line x1="9" y1="13" x2="11" y2="13" stroke="#6f9be0" stroke-width="1.2"/>
        </svg>
        <p class="contact__text">+971 4 000 3829<br>+971 50 000 4172</p>
      </div>

      <div class="contact__row">
        <svg class="contact__icon" viewBox="0 0 20 20" aria-hidden="true">
          <circle cx="10" cy="10" r="10" fill="#1a1c22"/>
          <rect x="5" y="6.5" width="10" height="7" fill="none" stroke="#6f9be0" stroke-width="1.2"/>
          <path d="M5 6.5 L10 10.5 L15 6.5" fill="none" stroke="#6f9be0" stroke-width="1.2"/>
        </svg>
        <p class="contact__text">khalid@corvane-example.ae</p>
      </div>
    </div>
  </section>

  <section class="card card--back" aria-label="Business card back">
    <div class="wordmark"><span class="wordmark__square"></span>Corvane Holdings</div>
    <div class="website">
      <span class="website__line"></span>
      <span class="website__text">www.corvane-example.ae</span>
      <span class="website__line"></span>
    </div>
  </section>

</main>
</body>
</html>
```